KIVO Cosmetics LABELS

one good design wanted for the KIVO COSMETICS brand.

These are cosmetics and detergents. The labels should be about 3" wide and 4" deep. It must be colorful and interesting with some art on it. Flowers, girl, ? anything.

The word KIVO should guide your thinking a little.

It has to be bold and with striking colors. The attached images are there only as a guide of images we like and the logos are there, so you can see what we have already.

Ask any further questions please.

This design should be colorful and not finicky

Reason: Ready to work with any designer - through Brief Harbor - for other projects.

some intriguing graphics, images or something 'wow' is wanted in the designs

Those wanting something different and economic.

Cosmetics

• Each label in a range is to be the same 'ish and to allow space for the name of the individual product to be added; such as Seaweed Shampoo.

Use of the logo will be all labels but small in a corner, or ...

USE OF THE SHOWN IMAGES, SHOULD BE THERE BUT NOT PROMINENTLY

```html
<!DOCTYPE html>
<html lang="en">
<head>
<meta charset="utf-8">
<title>KIVO Cosmetics – Seaweed label range</title>
<link rel="stylesheet" href="https://fonts.googleapis.com/css2?family=Barlow:wght@300&family=Inter:wght@200;900&display=swap">
<style>
  :root {
    --paper: #ffffff;
    --caption: #9a9a9a;
    --magenta: #e0127e;
    --magenta-soft: #e76aa9;
    --pink-glow: rgba(232, 40, 140, 0.55);
    --pink-haze: rgba(246, 184, 214, 0.6);
    --plum-glow: rgba(156, 42, 124, 0.4);
    --mint-light: #eef5f2;
    --mint: #b9d8cc;
    --mint-deep: #9cc8b8;
    --logo-box: #000000;
    --logo-text: #ffffff;
  }
  * { margin: 0; padding: 0; box-sizing: border-box; }
  html, body { width: 1200px; height: 800px; overflow: hidden; background: var(--paper); }
  .board { position: relative; width: 1200px; height: 800px; }
  .board-caption {
    position: absolute; left: 36px; top: 34px;
    font-family: "Barlow", sans-serif; font-weight: 300;
    font-size: 14px; letter-spacing: 0.6px; color: var(--caption);
  }
  .label {
    position: absolute; top: 196px; width: 305px; height: 407px; overflow: hidden;
    background:
      repeating-linear-gradient(90deg, rgba(255,255,255,0.18) 0 14px, rgba(255,255,255,0) 14px 38px, rgba(120,170,150,0.12) 38px 46px, rgba(255,255,255,0) 46px 70px),
      linear-gradient(110deg, var(--mint-light) 0%, var(--mint) 55%, var(--mint-deep) 100%);
  }
  .label--shampoo { left: 85px; }
  .label--conditioner { left: 447px; }
  .label--shower-gel { left: 809px; }
  .label-art {
    position: absolute; left: 12px; top: 14px; width: 281px; height: 318px;
    border-radius: 50%;
    background:
      radial-gradient(closest-side, var(--pink-glow), var(--pink-haze) 55%, rgba(246,184,214,0) 100%);
  }
  .label--conditioner .label-art {
    background: radial-gradient(closest-side, var(--pink-haze), var(--pink-glow) 60%, rgba(246,184,214,0) 100%);
  }
  .label--shower-gel .label-art {
    background: radial-gradient(closest-side, var(--pink-glow), var(--plum-glow) 55%, rgba(156,42,124,0) 100%);
  }
  .product-range {
    position: absolute; left: 9px; top: 342px;
    font-family: "Inter", sans-serif; font-weight: 900; font-size: 44px;
    letter-spacing: -0.8px; line-height: 1; color: var(--magenta);
  }
  .product-name {
    position: absolute; left: 9px; top: 377px;
    font-family: "Inter", sans-serif; font-weight: 200; font-size: 24px;
    letter-spacing: -0.6px; line-height: 1; color: var(--magenta-soft);
  }
  .brand-mark {
    position: absolute; left: 243px; top: 345px; width: 53px; height: 53px;
    background: var(--logo-box); display: flex; align-items: flex-end; justify-content: center;
    padding-bottom: 9px;
    font-family: "Inter", sans-serif; font-weight: 900; font-size: 17px;
    color: var(--logo-text); letter-spacing: -0.5px;
  }
</style>
</head>
<body>
<main class="board">
  <p class="board-caption">PROJECT KIVO COSMETICS LOGO / JUN 2013</p>

  <article class="label label--shampoo">
    <div class="label-art" role="img" aria-label="Illustration of overlapping pink and plum bubbles"></div>
    <h2 class="product-range">SEAWEED</h2>
    <p class="product-name">SHAMPOO</p>
    <div class="brand-mark">KIVO</div>
  </article>

  <article class="label label--conditioner">
    <div class="label-art" role="img" aria-label="Illustration of pink bubbles and pale rings"></div>
    <h2 class="product-range">SEAWEED</h2>
    <p class="product-name">CONDITIONER</p>
    <div class="brand-mark">KIVO</div>
  </article>

  <article class="label label--shower-gel">
    <div class="label-art" role="img" aria-label="Illustration of pink and plum bubbles with pale rings"></div>
    <h2 class="product-range">SEAWEED</h2>
    <p class="product-name">SHOWER GEL</p>
    <div class="brand-mark">KIVO</div>
  </article>
</main>
</body>
</html>
```